Business card por a urban DJ, up scale audience target

Need a sober design, modern, conservative colors but i can consider some options, y play rnb, hip hop, EDM and top40.

Business card for contact and personal info, double sided, use logo attrached please; im 42 so i need a card acording to my age an target audience.

Target Market(s)

Adult people, up scale audience

Industry/Entity Type

Music Download

Contact Information for Business Card

Cel (318) 5024471963 www.kelvarodun.com

Requirements
Must have
• open mind
Nice to have
• open mind
Should not have
• DJ

```html
<!DOCTYPE html>
<html lang="en">
<head>
<meta charset="utf-8">
<title>Kelvaro Business Card</title>
<link href="https://fonts.googleapis.com/css2?family=Open+Sans:wght@400;600;800&display=swap" rel="stylesheet">
<style>
  :root {
    --backdrop: #2b2b2b;
    --ink: #3b3635;
    --frame-light: #d2cfd0;
    --paper: #f7f7f7;
    --line: #ffffff;
  }
  html, body {
    margin: 0;
    padding: 0;
    width: 1200px;
    height: 1189px;
    overflow: hidden;
    background: var(--backdrop);
    font-family: "Open Sans", Arial, sans-serif;
  }
  .canvas {
    position: relative;
    width: 1200px;
    height: 1189px;
  }
  .card {
    position: absolute;
    width: 700px;
    height: 400px;
    box-shadow: 0 12px 30px rgba(0,0,0,0.45);
  }
  .card > .card-shapes { position: absolute; inset: 0; }
  .card-front { left: 110px; top: 110px; }
  .card-back { left: 390px; top: 650px; }

  .brand {
    position: absolute;
    margin: 0;
    color: var(--ink);
    font-weight: 800;
    letter-spacing: 2px;
    line-height: 1;
  }
  .card-front .brand {
    left: 0; right: 0; top: 168px;
    text-align: center;
    font-size: 60px;
  }
  .card-back .brand {
    left: 42px; top: 112px;
    font-size: 44px;
  }
  .holder {
    position: absolute;
    left: 350px; top: 50px;
    color: var(--ink);
  }
  .holder-name {
    margin: 0;
    font-size: 24px;
    font-weight: 400;
    letter-spacing: 0.5px;
    line-height: 1.1;
  }
  .holder-role {
    margin: 0;
    font-size: 15px;
    font-weight: 600;
    line-height: 1.2;
  }
  .contacts {
    position: absolute;
    left: 360px; top: 196px;
    margin: 0; padding: 0;
    list-style: none;
    color: var(--ink);
    font-size: 19px;
  }
  .contacts li {
    display: flex;
    align-items: center;
    gap: 10px;
    height: 34px;
  }
  .contact-icon {
    width: 18px;
    height: 18px;
    flex: none;
    fill: var(--ink);
  }
</style>
</head>
<body>
<main class="canvas">

  <section class="card card-front" aria-label="Card front">
    <svg class="card-shapes" viewBox="0 0 700 400" width="700" height="400">
      <rect width="700" height="400" fill="var(--frame-light)"/>
      <polygon points="0,250 0,400 330,400 360,370 40,370 40,270" fill="var(--ink)"/>
      <polygon points="480,0 700,0 700,140 660,110 660,30 500,30" fill="var(--ink)"/>
      <rect x="40" y="30" width="620" height="340" fill="var(--paper)"/>
      <polyline points="40,270 40,370 340,370" fill="none" stroke="var(--line)" stroke-width="3"/>
      <polyline points="500,30 660,30 660,110" fill="none" stroke="var(--line)" stroke-width="3"/>
    </svg>
    <p class="brand">KELVARO</p>
  </section>

  <section class="card card-back" aria-label="Card back">
    <svg class="card-shapes" viewBox="0 0 700 400" width="700" height="400">
      <rect width="700" height="400" fill="var(--ink)"/>
      <polygon points="380,0 700,0 700,40 600,40 560,20" fill="var(--frame-light)"/>
      <polygon points="0,230 0,400 360,400 310,350 310,260 180,260 150,290 60,290" fill="var(--frame-light)"/>
      <polygon points="30,30 560,30 600,40 640,40 640,330 340,330 310,350 310,260 180,260 150,290 60,290 30,230" fill="var(--paper)"/>
      <polyline points="560,30 600,40 640,40" fill="none" stroke="var(--line)" stroke-width="3"/>
      <polyline points="60,290 150,290 180,260 310,260 310,350" fill="none" stroke="var(--line)" stroke-width="3"/>
    </svg>
    <p class="brand">KELVARO</p>
    <div class="holder">
      <p class="holder-name">JONATHAN DOE</p>
      <p class="holder-role">Managing Director</p>
    </div>
    <ul class="contacts">
      <li>
        <svg class="contact-icon" viewBox="0 0 24 24" aria-hidden="true"><path d="M3 9c0-3 4-5 9-5s9 2 9 5v2h-5V9c-1-.6-2.5-1-4-1s-3 .4-4 1v2H3zM6 13h12l2 7H4z"/></svg>
        <span>(318) 5024471963</span>
      </li>
      <li>
        <svg class="contact-icon" viewBox="0 0 24 24" aria-hidden="true"><path d="M2 5h20v14H2zm2 2v.5l8 6 8-6V7zm0 3v7h16v-7l-8 6z"/></svg>
        <span>info@yourwebsite.com</span>
      </li>
      <li>
        <svg class="contact-icon" viewBox="0 0 24 24" aria-hidden="true"><circle cx="12" cy="12" r="9" fill="none" style="stroke:var(--ink)" stroke-width="2"/><path d="M3 12h18M12 3c3 3 3 15 0 18M12 3c-3 3-3 15 0 18" fill="none" style="stroke:var(--ink)" stroke-width="1.5"/></svg>
        <span>www.kelvarodun.com</span>
      </li>
    </ul>
  </section>

</main>
</body>
</html>
```